Business Card Design Project

We require a business card template to cover basic contact information - our company logo, names of employees, title, mobile and email.

Target Market(s)

Corporate

Industry/Entity Type

Business

Font styles to use
Sans Serif

Requirements
Nice to have
• Thinking it would be great just to have the logo taking up approximately half the space (so it goes as far across the top of the card as possible) and then contact details in the lower half of the card. Keen just to use only the two colours in the logo, on a white background.
Should not have
• No fussy drawings

```html
<!DOCTYPE html>
<html lang="en">
<head>
<meta charset="utf-8">
<title>Kestrel Developments – Business Card</title>
<link rel="stylesheet" href="https://fonts.googleapis.com/css2?family=Andika:wght@400&display=swap">
<style>
  :root {
    --brand-teal: #1fa3b5;
    --brand-navy: #2d5f98;
    --ink: #111111;
    --paper: #ffffff;
    --edge: #222222;
  }
  html, body {
    margin: 0;
    padding: 0;
    width: 705px;
    height: 1200px;
    overflow: hidden;
    background: var(--paper);
  }
  .card {
    position: relative;
    width: 705px;
    height: 1200px;
    box-sizing: border-box;
    border: 2px solid var(--edge);
    border-radius: 34px;
    background: var(--paper);
    font-family: "Andika", sans-serif;
    overflow: hidden;
  }
  .brand {
    position: absolute;
    left: 40px;
    right: 40px;
    top: 78px;
    color: var(--brand-teal);
    font-weight: 400;
  }
  .brand-name {
    display: block;
    font-size: 168px;
    line-height: 1;
    letter-spacing: -2px;
  }
  .brand-tagline {
    display: block;
    text-align: right;
    font-size: 40px;
    line-height: 1;
    margin-top: 2px;
    margin-right: 4px;
  }
  .contact {
    position: absolute;
    left: 48px;
    top: 820px;
    color: var(--ink);
  }
  .contact-name {
    margin: 0;
    font-size: 58px;
    font-weight: 400;
    line-height: 1;
    color: var(--brand-teal);
  }
  .contact-title {
    margin: 8px 0 0;
    font-size: 30px;
    line-height: 1.1;
  }
  .contact-lines {
    margin: 62px 0 0;
    padding: 0;
    list-style: none;
    font-size: 31px;
    line-height: 1.5;
  }
  .footer-bar {
    position: absolute;
    left: 0;
    bottom: 64px;
    width: 705px;
    height: 30px;
  }
</style>
</head>
<body>
  <div class="card">
    <div class="brand">
      <span class="brand-name">Kestrel</span>
      <span class="brand-tagline">developments</span>
    </div>

    <div class="contact">
      <h1 class="contact-name">Daniel.R</h1>
      <p class="contact-title">Director</p>
      <ul class="contact-lines">
        <li>M: 0198765432</li>
        <li>E: daniel.reed@example.com</li>
      </ul>
    </div>

    <svg class="footer-bar" viewBox="0 0 705 30" aria-hidden="true">
      <rect x="6" y="0" width="405" height="30" fill="var(--brand-navy)"/>
      <rect x="413" y="0" width="75" height="30" fill="var(--brand-teal)"/>
      <rect x="490" y="0" width="19" height="30" fill="var(--brand-navy)"/>
      <rect x="521" y="0" width="19" height="30" fill="var(--brand-navy)"/>
    </svg>
  </div>
</body>
</html>
```